Zielgruppe
Wir sind ein Familienweingut in 11. Generation. Durch das lange Bestehen des Betriebes haben wir eine klassische Linie der Weine. Jedoch haben wir neben unserer Classic Linie eine komplett junge und modernere Linie im Weingut wie z.B.: ein Cüvee mit dem Namen 'Wolkentanz' (besteht aus 3 Sorten und ein Bezug zu unseren Freilandschweinen am Weingut wird hergestellt) Durch unsere zwei Produktlinien können wir eine sehr hohe Zielgruppe erreichen. Nun erweitert sich unsere moderne Linie um einen Rosé, dieser soll wie die anderen das jüngere Puplikum ansprechen.
Aufgabenstellung
Wir brauchen ein Etikett für unseren Rose mit dem Namen 'Sky Dash': Pink setzt sich durch die Farbe des Weines zusammen und das Pin-up soll dies verkörpern. Es soll sich ein Pin-up Girl auf dem Etikett befinden, wo auch eine Verbindung zum Wein an sich hergestellt wird. Der Kreativität sind keine Grenzen gesetzt. Auch der Name des Weines muss am Etikett stehen.
Zusätzliche Infos:
Die Maße des Etiketts betragen 113x97mm.
alle weiteren Daten befinden sich bei der Flasche auf dem Rückenetikett; sprich, es geht rein nur um das vordere Etikett und dessen grafische Darstellung.
Danke im Voraus.
Weingut Zwirnlehner

```html
<!DOCTYPE html>
<html lang="de">
<head>
<meta charset="utf-8">
<title>Sky Dash – Rosé Etikett</title>
<link rel="stylesheet" href="https://fonts.googleapis.com/css2?family=Poppins:wght@400;600;700&display=swap">
<style>
  :root {
    --canvas: #ffffff;
    --label-pink: #fdd3df;
    --band-dark: #373737;
    --ink: #3a3a3a;
    --gold: #b8952e;
    --gold-light: #e3c76a;
    --art-red: #d9452f;
    --art-skin: #f3d9c4;
    --art-olive: #c9b44a;
    --art-blue: #b9dde6;
  }
  * { margin: 0; padding: 0; box-sizing: border-box; }
  html, body {
    width: 1200px;
    height: 1200px;
    overflow: hidden;
    background: var(--canvas);
  }
  body {
    position: relative;
    font-family: "Poppins", sans-serif;
    color: var(--ink);
  }
  .label {
    position: absolute;
    left: 50px;
    top: 307px;
    width: 1100px;
    height: 586px;
    background: var(--label-pink);
    overflow: hidden;
  }
  .band { position: absolute; left: 0; width: 100%; background: var(--band-dark); }
  .band--top { top: 0; height: 28px; }
  .band--middle { top: 288px; height: 175px; }
  .band--bottom { top: 558px; height: 28px; }
  .gold-rule {
    position: absolute;
    left: 0;
    top: 463px;
    width: 100%;
    height: 9px;
    background: linear-gradient(90deg, var(--gold), var(--gold-light) 45%, var(--gold) 70%, var(--gold-light));
    z-index: 2;
  }
  .product-type {
    position: absolute;
    left: 52px;
    top: 92px;
    font-size: 18px;
    font-weight: 700;
    letter-spacing: 0.5px;
  }
  .volume {
    position: absolute;
    left: 52px;
    top: 134px;
    font-size: 17px;
    font-weight: 400;
  }
  .wine-name {
    position: absolute;
    left: 504px;
    top: 50px;
    transform: translateX(-50%);
    font-size: 42px;
    line-height: 52px;
    font-weight: 700;
    letter-spacing: 1px;
    white-space: nowrap;
    z-index: 3;
  }
  .ingredients {
    position: absolute;
    right: 52px;
    top: 88px;
    width: 205px;
    text-align: right;
    font-size: 17px;
    line-height: 28px;
  }
  .pinup-art {
    position: absolute;
    left: 326px;
    top: 122px;
    width: 396px;
    height: 341px;
    border-radius: 45% 45% 4px 4px / 30% 30% 4px 4px;
    background: linear-gradient(160deg, var(--art-red) 0%, var(--art-skin) 35%, var(--art-olive) 60%, var(--art-blue) 100%);
    z-index: 1;
  }
  .wine-style {
    position: absolute;
    left: 504px;
    top: 502px;
    transform: translateX(-50%);
    font-size: 19px;
    font-weight: 600;
  }
  .winery {
    position: absolute;
    right: 52px;
    top: 502px;
    font-size: 18px;
    font-weight: 700;
    letter-spacing: 0.5px;
  }
</style>
</head>
<body>
  <main class="label">
    <div class="band band--top"></div>
    <div class="band band--middle"></div>
    <div class="gold-rule"></div>
    <div class="band band--bottom"></div>

    <p class="product-type">ROSE FRAGANCE</p>
    <p class="volume">50mL</p>

    <h1 class="wine-name">SKY DASH</h1>

    <p class="ingredients">Inhalt: Ethyl Alcohol, Coumarin, Benzyl Benzoate, Distill Water, Rose Oil, Pink Extract</p>

    <div class="pinup-art" role="img" aria-label="Pin-up illustration: a red-haired woman in olive stockings and red heels reclining on patterned cushions beside a wine glass"></div>

    <p class="wine-style">ROSÈ</p>
    <p class="winery">WEINGUT XY</p>
  </main>
</body>
</html>
```